We have 'joined together' 6 micro-sites with a common theme. Looking to upgrade the design of a total of 26 pages on the abovementioned sites, whilst maintaining a common look and feel.

Goal is to improve customer experience and conversion rate, whilst maintaining Quenbo rankings. New design to be responsive to different devices and SEO optimised

We prefer simple designs with the cleaness of Zorvane.com, however with more descriptive text. Target audience are business managers and owners, so site should convey professional capability, with a hint of playfulness. After all data can be fun? No?

See attached doc for further details.

Update: 19/8/2014. Following further consideration, the HTML coding no longer required. Once design is finalised, we require a PSD file for each page showing the full page layout, including all images and icons. We will extract the relevant bits from the PSD and do the coding and css inhouse.
Updates

Hi All The Mirel Group - PSD Design Only. HTML no longer required Following further consideration, the HTML / Css coding aspect of the project NO longer required. Once design is finalised, we require a PSD file from you for each of the 26 web pages, showing the page layout and including all images and icons. If one page layout is the same as another, then we request that you just supply images and icons for that page in a PSD file. We will then extract the relevant bits from the PSD and we will do the coding and css inhouse. Our main aim is to get an awesome, blow-your-sox-off design that compels users to convert. Many thanks in anticipation Oliver.

Project Deadline Extended
Reason: Changed deliverables from PSD, HTML and Coding t o PSD only. Hopefully this change will allow previous designers who were not interested to reconsider. Many thanks Oliver

Target Market(s)

Target market is business & IT managers within Australian organisations who are having problems with their data. Site must convey the impression that we are:
1) Very capable
2) Professional in our dealings
3) Reliable & trustworthy
4) Just a little bit quirky

Aprox. 60% of users are female, 40% male. Typically in the 30 to 55 year old bracket.

Number 1 requirements is that we don't embarrass our clients in any way.
2nd is that we do a good high quality job, delivering a good result.

We are not the cheapest nor the most expensive data shop around. We offer good value-for-money solutions. We are also reliable, friendly and available

Industry/Entity Type

Business

Font styles to use
Sans Serif

Requirements
Must have
• Simple yet information dense design. The "who we are" and "what we do" to be immediately visible above the fold. Images to be high quality. Good usability.
Simple navigation structure. Easy for users to find the info that they want.

In summary a simple, but good looking site, that compels users to contact us
Should not have
• No flash, fancy automation, rotating images, pop-ups etc.

```html
<!DOCTYPE html>
<html lang="en">
<head>
<meta charset="utf-8">
<title>The Mirel Group</title>
<link href="https://fonts.googleapis.com/css2?family=Bitter:wght@400;700&family=Open+Sans:wght@400;600;700&family=Roboto:wght@400;500;700&display=swap" rel="stylesheet">
<style>
:root{
  --orange:#f27022;
  --ink:#333;
  --body:#555;
  --muted:#888;
  --line:#e4e4e4;
  --panel:#f7f7f7;
  --dark:#161616;
  --footer:#232323;
  --white:#fff;
}
*{box-sizing:border-box;margin:0;padding:0}
html,body{width:1200px;height:2241px;overflow:hidden}
body{position:relative;background:var(--white);font-family:"Roboto",Arial,sans-serif;color:var(--body)}
.abs{position:absolute}

.topbar{left:0;top:0;width:1200px;height:38px;background:var(--dark);font-size:11px;color:#bbb;display:flex;align-items:center;justify-content:flex-end;padding-right:135px;gap:16px}
.topbar .accent-line{position:absolute;left:500px;top:0;width:560px;height:2px;background:#555}
.topbar .item{display:flex;align-items:center;gap:6px}
.topbar .orange{color:var(--orange);font-weight:500}

.mainnav{left:0;top:38px;width:1200px;height:65px;background:var(--white);display:flex;justify-content:center;align-items:center}
.mainnav a{font-size:12px;color:#333;text-decoration:none;padding:0 15px;height:65px;display:flex;align-items:center;border-left:1px solid #eee}
.mainnav a:first-child{border-left:none}
.mainnav a.current{color:var(--orange);font-style:italic}

.hero{left:0;top:103px;width:1200px;height:689px;background:linear-gradient(180deg,#8a9694 0%,#7d8987 55%,#2a2f35 78%,#1c2026 100%)}
.hero-title{left:0;top:130px;width:1200px;text-align:center;font-family:"Open Sans",Arial,sans-serif;font-weight:600;font-size:72px;line-height:84px;color:var(--white)}
.hero-sub{left:0;top:213px;width:1200px;text-align:center;font-family:"Open Sans",Arial,sans-serif;font-size:21px;color:var(--white)}

.intro-panel{left:111px;top:768px;width:978px;height:400px;background:var(--white)}
.eyebrow{left:0;top:786px;width:1200px;text-align:center;font-size:11px;letter-spacing:1px;color:#999;font-weight:500}
.section-heading{left:0;top:800px;width:1200px;text-align:center;font-family:"Bitter",Georgia,serif;font-weight:700;font-size:32px;color:var(--orange)}
.rule{left:138px;top:854px;width:924px;height:1px;background:var(--line)}

.service{width:300px;height:100px}
.service .badge{position:absolute;left:0;top:0;width:90px;height:90px;border-radius:50%;background:var(--white);box-shadow:0 2px 8px rgba(0,0,0,.12);display:flex;align-items:center;justify-content:center}
.service h3{position:absolute;left:110px;top:6px;font-family:"Bitter",Georgia,serif;font-weight:700;font-size:16px;color:var(--ink)}
.service p{position:absolute;left:110px;top:34px;width:170px;font-size:11px;line-height:17px;color:var(--body)}

.services-copy{left:111px;top:1208px;width:489px;height:280px;background:var(--panel);padding:10px 14px}
.col-heading{font-family:"Bitter",Georgia,serif;font-weight:700;font-size:22px;color:var(--ink);margin-bottom:6px}
.services-copy p{font-size:11px;line-height:17px;color:var(--body);margin-bottom:6px}
.readmore{display:flex;align-items:center;gap:6px;font-size:11px;font-weight:700;color:var(--orange);margin-top:8px}

.benefits{left:600px;top:1208px;width:465px;height:280px;background:var(--panel);padding:4px 8px}
.benefits .intro{font-size:10.5px;line-height:16px;color:var(--body)}
.benefits .intro mark{background:#333;color:var(--white);padding:1px 2px}
.benefit{display:flex;gap:14px;padding:9px 6px;border-bottom:1px solid var(--line);font-size:12px;line-height:16.5px;color:#7b8592}
.benefit:last-child{border-bottom:none}
.benefit svg{flex:none;margin-top:3px}

.reviews-heading{left:0;top:1512px;width:1200px;text-align:center;font-family:"Bitter",Georgia,serif;font-weight:700;font-size:32px;color:var(--orange)}
.rule2{left:138px;top:1568px;width:924px;height:1px;background:var(--line)}

.contact{left:96px;top:1585px;width:504px;height:318px;background:var(--panel);padding:6px 29px}
.contact .field{width:461px;height:32px;border:1px solid var(--line);background:var(--white);font-size:11px;color:#aaa;padding:0 10px;display:flex;align-items:center;margin-bottom:10px}
.contact .field.message{height:118px;align-items:flex-start;padding-top:10px}
.send{display:inline-flex;align-items:center;justify-content:center;width:102px;height:32px;background:var(--orange);color:var(--white);font-size:11px;font-weight:500;border-radius:2px}

.testimonials{left:600px;top:1598px;width:483px;height:290px;background:var(--panel)}
.quote{position:absolute;left:6px;width:460px}
.quote .mark{position:absolute;left:0;top:-6px;font-family:"Bitter",Georgia,serif;font-size:70px;line-height:70px;color:#ccc}
.quote blockquote{position:absolute;left:20px;top:0;width:440px;font-size:13.5px;line-height:24px;font-weight:500;color:#222}
.quote cite{position:absolute;left:20px;top:86px;width:440px;font-style:normal;font-size:11px;color:var(--orange);display:flex;align-items:center;gap:8px;border-top:1px solid var(--line);padding-top:8px}

.footer{left:0;top:1952px;width:1200px;height:237px;background:var(--footer)}
.footer-brand{left:130px;top:1975px;font-family:"Open Sans",Arial,sans-serif;font-weight:600;font-size:27px;color:var(--white)}
.footer-about{left:130px;top:2012px;width:220px;font-size:12px;line-height:20px;color:#ddd}
.socials{left:130px;top:2085px;display:flex;gap:6px}
.socials span{width:36px;height:36px;background:var(--white)}
.footer-nav-title{left:370px;top:1985px;font-family:"Bitter",Georgia,serif;font-weight:700;font-size:17px;color:var(--white)}
.footer-links{left:370px;top:2016px;display:grid;grid-template-columns:repeat(7,103px);row-gap:11px}
.footer-links a{font-size:11px;color:var(--orange);text-decoration:none}
.copyright{left:0;top:2189px;width:1200px;height:52px;background:var(--footer);border-top:1px solid #333;display:flex;align-items:center;justify-content:center;font-size:11px;color:#ccc}
</style>
</head>
<body>

<header class="abs topbar">
  <span class="accent-line"></span>
  <span>Contact Us:</span>
  <span class="item orange">
    <svg width="10" height="10" viewBox="0 0 10 10"><path d="M2 0.5l2 2-1 1.2c.6 1.3 1.6 2.3 2.8 2.8l1.2-1 2 2-1.4 1.6C4.5 9.3.7 5.5.6 1.9z" fill="#bbb"/></svg>
    1300 415 270
  </span>
  <span class="item orange">
    <svg width="11" height="9" viewBox="0 0 11 9"><rect x=".5" y=".5" width="10" height="8" fill="none" stroke="#bbb"/><path d="M.5.5l5 4 5-4" fill="none" stroke="#bbb"/></svg>
    hello@mirelgroup.example
  </span>
</header>

<nav class="abs mainnav">
  <a>Home</a><a>Data Analysis</a><a>Data Cleansing</a><a>Data Mining</a><a>Data Scraping</a><a>Data Warehouses</a><a>Blog</a><a class="current">Contact Us</a>
</nav>

<div class="abs hero" role="img" aria-label="Photograph of two children in suits and goggles wearing makeshift metal helmets, sitting at a desk with a vintage meter"></div>
<h1 class="abs hero-title">The Mirel Group</h1>
<p class="abs hero-sub">Helping You Creatively Generate Real Value from Your Data</p>

<div class="abs intro-panel"></div>
<p class="abs eyebrow">MORBI IN SEM QUIS DUI PLACERAT</p>
<h2 class="abs section-heading">Reap the Rewards from a Data Project</h2>
<div class="abs rule"></div>

<div class="abs service" style="left:142px;top:903px">
  <div class="badge"><svg width="44" height="40" viewBox="0 0 44 40"><rect x="4" y="24" width="6" height="14" fill="#f27022"/><rect x="14" y="18" width="6" height="20" fill="#f27022"/><rect x="24" y="12" width="6" height="26" fill="#f27022"/><rect x="34" y="6" width="6" height="32" fill="#f27022"/><path d="M3 18L14 10l8 4L38 2" fill="none" stroke="#f27022" stroke-width="2.5"/></svg></div>
  <h3>Data Analysis</h3>
  <p>Vitae adipiscing turpis. Aenean ligula nibh in, molestie id viverra a, dapibus at dolor.</p>
</div>
<div class="abs service" style="left:456px;top:903px">
  <div class="badge"><svg width="40" height="40" viewBox="0 0 40 40"><path d="M28 4l6 6-12 12-6-6z" fill="#f27022"/><path d="M14 18l8 8-8 12H4l-2-4z" fill="none" stroke="#f27022" stroke-width="2.5"/><circle cx="8" cy="8" r="2" fill="#f27022"/><circle cx="34" cy="28" r="2" fill="#f27022"/></svg></div>
  <h3>Data Cleansing</h3>
  <p>Vitae adipiscing turpis. Aenean ligula nibh in, molestie id viverra a, dapibus at dolor.</p>
</div>
<div class="abs service" style="left:771px;top:903px">
  <div class="badge"><svg width="42" height="42" viewBox="0 0 42 42"><circle cx="17" cy="17" r="13" fill="none" stroke="#f27022" stroke-width="3"/><path d="M27 27l11 11" stroke="#f27022" stroke-width="5" stroke-linecap="round"/><path d="M17 11v12M11 17h12" stroke="#f27022" stroke-width="3"/></svg></div>
  <h3>Data Mining</h3>
  <p>Vitae adipiscing turpis. Aenean ligula nibh in, molestie id viverra a, dapibus at dolor.</p>
</div>
<div class="abs service" style="left:142px;top:1047px">
  <div class="badge"><svg width="44" height="40" viewBox="0 0 44 40"><rect x="3" y="3" width="38" height="26" rx="2" fill="none" stroke="#f27022" stroke-width="3"/><rect x="18" y="29" width="8" height="6" fill="#f27022"/><rect x="12" y="35" width="20" height="3" fill="#f27022"/><circle cx="22" cy="16" r="5" fill="#f27022"/></svg></div>
  <h3>Data Scraping</h3>
  <p>Vitae adipiscing turpis. Aenean ligula nibh in, molestie id viverra a, dapibus at dolor.</p>
</div>
<div class="abs service" style="left:456px;top:1047px">
  <div class="badge"><svg width="34" height="42" viewBox="0 0 34 42"><ellipse cx="17" cy="7" rx="15" ry="5" fill="#f27022"/><path d="M2 11c0 3 7 5 15 5s15-2 15-5v7c0 3-7 5-15 5S2 21 2 18z" fill="#f27022"/><path d="M2 22c0 3 7 5 15 5s15-2 15-5v7c0 3-7 5-15 5S2 32 2 29z" fill="#f27022"/></svg></div>
  <h3>Data Warehouse</h3>
  <p>Vitae adipiscing turpis. Aenean ligula nibh in, molestie id viverra a, dapibus at dolor.</p>
</div>
<div class="abs service" style="left:771px;top:1047px">
  <div class="badge"><svg width="38" height="42" viewBox="0 0 38 42"><rect x="14" y="2" width="20" height="26" fill="none" stroke="#f27022" stroke-width="2.5"/><rect x="9" y="8" width="20" height="26" fill="#fff" stroke="#f27022" stroke-width="2.5"/><rect x="4" y="14" width="20" height="26" fill="#fff" stroke="#f27022" stroke-width="2.5"/></svg></div>
  <h3>Data Resources</h3>
  <p>Vitae adipiscing turpis. Aenean ligula nibh in, molestie id viverra a, dapibus at dolor.</p>
</div>

<section class="abs services-copy">
  <h2 class="col-heading">Data Services</h2>
  <p>The Mirel Group is a Melbourne based business offering a comprehensive range of data services. We specialise in data analysis, data cleansing, data mining, data scraping and data warehouses. Our goal is to help you extract value from your data in the form of pragmatic insights, trends and relationships. And then to analyse, interpret and use these findings in innovative ways that empower you to manage your organisation for greater profit, with improved decision-making and enhanced strategic, tactical and operational insight.</p>
  <p>The Mirel Group is a Melbourne based business offering a comprehensive range of data services. We specialise in data analysis, data cleansing, data mining, data scraping and data warehouses. Our goal is to help you extract value from your data in the form of pragmatic insights, trends and relationships. And then to analyse, interpret and use these findings in innovative ways that empower you to manage your organisation for greater profit, with improved decision-making and enhanced strategic, tactical and operational insight.</p>
  <div class="readmore"><svg width="10" height="10" viewBox="0 0 10 10"><path d="M4 6L6 4M3 5L1.5 6.5a1.4 1.4 0 002 2L5 7M5 3l1.5-1.5a1.4 1.4 0 012 2L7 5" fill="none" stroke="#333" stroke-width="1.2"/></svg>Read more</div>
</section>

<section class="abs benefits">
  <h2 class="col-heading" style="margin-bottom:4px">Your Benefits</h2>
  <p class="intro">Our core speciality is solving business problems that require complex data analysis, cleansing, mining or modelling techniques. <mark>core speciality is solving business problems that require complex data analysis, cleansing, mining or modelling techniques.</mark> Your benefits include:</p>
  <div class="benefit">
    <svg width="10" height="13" viewBox="0 0 10 13"><path d="M5 12S1 7 1 5a4 4 0 018 0c0 2-4 7-4 7z" fill="none" stroke="#555" stroke-width="1.3"/><circle cx="5" cy="5" r="1.4" fill="#555"/></svg>
    <span>Fast ROI: Quick access to skilled data professionals, without the overhead of building and maintaining your own infrastructure and team. Our fees are typically small in contrast to the additional profits or savings that our projects generate for our clients.</span>
  </div>
  <div class="benefit">
    <svg width="10" height="13" viewBox="0 0 10 13"><path d="M5 12S1 7 1 5a4 4 0 018 0c0 2-4 7-4 7z" fill="none" stroke="#555" stroke-width="1.3"/><circle cx="5" cy="5" r="1.4" fill="#555"/></svg>
    <span>Innovative practical solutions: We find smart ways to extract useful information from incomplete and disorganised data. We also have extensive industry experience AND the quantitative rigour to generate innovative yet pragmatic value-adding solutions.</span>
  </div>
</section>

<h2 class="abs reviews-heading">WHAT OTHERS ARE SAYING</h2>
<div class="abs rule2"></div>

<section class="abs contact">
  <h2 class="col-heading" style="font-size:19px">Contact Us</h2>
  <div class="field">Your name</div>
  <div class="field">Your email</div>
  <div class="field">Subject</div>
  <div class="field message">Message</div>
  <div class="send">Send message</div>
</section>

<section class="abs testimonials">
  <div class="quote" style="top:20px">
    <span class="mark">&#8220;</span>
    <blockquote>We were blown away by your professionalism, rapid turnaround time and high level of matching accuracy. I can't thank you enough and have no regrets in recommending you to anybody who asks.</blockquote>
    <cite><svg width="10" height="10" viewBox="0 0 10 10"><circle cx="5" cy="3" r="2.5" fill="#555"/><path d="M0 10c0-3 2-4.5 5-4.5s5 1.5 5 4.5z" fill="#555"/></svg>Tarvel Studio</cite>
  </div>
  <div class="quote" style="top:166px">
    <span class="mark">&#8220;</span>
    <blockquote>We were blown away by your professionalism, rapid turnaround time and high level of matching accuracy. I can't thank you enough and have no regrets in recommending you to anybody who asks.</blockquote>
    <cite><svg width="10" height="10" viewBox="0 0 10 10"><circle cx="5" cy="3" r="2.5" fill="#555"/><path d="M0 10c0-3 2-4.5 5-4.5s5 1.5 5 4.5z" fill="#555"/></svg>Tarvel Studio</cite>
  </div>
</section>

<footer class="abs footer"></footer>
<div class="abs footer-brand">The Mirel Group</div>
<p class="abs footer-about">Our goal is to help you extract value from your data in the form of pragmatic insights, trends and relationships.</p>
<div class="abs socials"><span></span><span></span><span></span><span></span><span></span></div>
<h3 class="abs footer-nav-title">Navigations</h3>
<div class="abs footer-links">
  <a>Navigation</a><a>Navigation</a><a>Navigation</a><a>Navigation</a><a>Navigation</a><a>Navigation</a><a>Navigation</a>
  <a>Navigation</a><a>Navigation</a><a>Navigation</a><a>Navigation</a><a>Navigation</a><a>Navigation</a><a>Navigation</a>
  <a>Navigation</a><a>Navigation</a><a>Navigation</a><a>Navigation</a><a>Navigation</a><a>Navigation</a><a>Navigation</a>
  <a>Navigation</a><a>Navigation</a><a>Navigation</a><a>Navigation</a><a>Navigation</a><a>Navigation</a><a>Navigation</a>
</div>
<div class="abs copyright">© 2014 The Mirel Group. All Rights Reserved.</div>

</body>
</html>
```